.

Target Market(s)

Young, male, tech savvy, cryptocurrency investors

Industry/Entity Type

Information Technology

Logo Text

.

Coding

Coded - Design and coding required

Number of Pages Required

1 page

Font styles to use
Sans Serif

Colors

Designer to choose colors to be used in the design.

Requirements
Must have
• .

```html
<!DOCTYPE html>
<html lang="en">
<head>
<meta charset="utf-8">
<title>Veltra network</title>
<link href="https://fonts.googleapis.com/css2?family=Mulish:wght@400;700;800&family=Noto+Serif:wght@400&display=swap" rel="stylesheet">
<style>
  :root {
    --blue-deep: #0f2487;
    --blue-mid: #1233b8;
    --blue-bright: #0b34d6;
    --navy-bar: rgba(8, 16, 52, 0.82);
    --navy-footer: rgba(10, 20, 62, 0.9);
    --button: #0a7cff;
    --white: #ffffff;
    --divider: rgba(255, 255, 255, 0.55);
  }
  * { margin: 0; padding: 0; box-sizing: border-box; }
  html, body { width: 1200px; height: 658px; overflow: hidden; background: var(--blue-deep); }
  .page {
    position: relative;
    width: 1200px;
    height: 658px;
    overflow: hidden;
    font-family: "Mulish", sans-serif;
    color: var(--white);
  }
  .hero-backdrop {
    position: absolute;
    inset: 0;
    background:
      radial-gradient(ellipse 60% 45% at 50% 0%, var(--blue-bright) 0%, rgba(11,52,214,0) 100%),
      radial-gradient(ellipse 80% 60% at 50% 70%, rgba(40,80,230,0.55) 0%, rgba(18,40,150,0) 100%),
      linear-gradient(180deg, var(--blue-mid) 0%, var(--blue-deep) 100%);
  }
  .menu-toggle { position: absolute; left: 1071px; top: 13px; }
  .brand {
    position: absolute;
    top: 178px;
    left: 0;
    width: 1200px;
    text-align: center;
    font-size: 50px;
    font-weight: 400;
    line-height: 1;
    letter-spacing: 0.5px;
  }
  .headline {
    position: absolute;
    top: 254px;
    left: 0;
    width: 1200px;
    text-align: center;
    font-size: 36px;
    font-weight: 800;
    line-height: 44px;
  }
  .cta {
    position: absolute;
    left: 539px;
    top: 357px;
    width: 122px;
    height: 35px;
    background: var(--button);
    border-radius: 2px;
    font-size: 15px;
    font-weight: 700;
    line-height: 35px;
    text-align: center;
    color: var(--white);
    text-decoration: none;
  }
  .slide-arrow { position: absolute; top: 268px; }
  .slide-arrow.prev { left: 96px; }
  .slide-arrow.next { left: 1086px; }
  .timeline {
    position: absolute;
    left: 97px;
    top: 450px;
    width: 1003px;
    height: 41px;
    background: var(--navy-bar);
    display: flex;
    align-items: center;
    font-family: "Noto Serif", serif;
  }
  .timeline-title {
    font-size: 27px;
    width: 146px;
    padding-left: 9px;
    height: 41px;
    line-height: 41px;
    border-right: 1px solid var(--divider);
    height: 38px;
    line-height: 38px;
  }
  .timeline-item {
    font-size: 11.5px;
    padding: 0 14px 0 11px;
    height: 27px;
    line-height: 27px;
    white-space: nowrap;
  }
  .timeline-item + .timeline-item { border-left: 1px solid var(--divider); }
  .timeline-item:nth-child(2) { width: 236px; }
  .timeline-item:nth-child(3) { width: 305px; }
  .site-footer {
    position: absolute;
    left: 0;
    top: 607px;
    width: 1200px;
    height: 51px;
    background: var(--navy-footer);
    font-size: 11px;
  }
  .copyright { position: absolute; left: 0; width: 1200px; top: 17px; text-align: center; }
  .page-code { position: absolute; left: 1123px; top: 19px; font-size: 11px; }
</style>
</head>
<body>
<main class="page">
  <div class="hero-backdrop" role="img" aria-label="Blue digital globe background with a glowing network of connected nodes"></div>

  <svg class="menu-toggle" width="30" height="21" viewBox="0 0 30 21" aria-label="Menu">
    <rect x="0" y="0" width="30" height="2.5" fill="#fff"/>
    <rect x="0" y="9" width="30" height="2.5" fill="#fff"/>
    <rect x="0" y="18" width="30" height="2.5" fill="#fff"/>
  </svg>

  <div class="brand">Veltra network</div>

  <h1 class="headline">The world’s most advanced blockchain<br>the widest token distribution</h1>

  <a class="cta" href="#">Sign Up Now</a>

  <svg class="slide-arrow prev" width="16" height="22" viewBox="0 0 16 22" aria-label="Previous">
    <polyline points="12,2 4,11 12,20" fill="none" stroke="#fff" stroke-width="2.6"/>
  </svg>
  <svg class="slide-arrow next" width="16" height="22" viewBox="0 0 16 22" aria-label="Next">
    <polyline points="4,2 12,11 4,20" fill="none" stroke="#fff" stroke-width="2.6"/>
  </svg>

  <section class="timeline">
    <div class="timeline-title">Time Line</div>
    <div class="timeline-item">Sept 2017 -&nbsp; Corvex Network Airdrop</div>
    <div class="timeline-item">Oct 2017 -&nbsp; Talmar Network Linked Address Airdrop</div>
    <div class="timeline-item">Nov 2017 -&nbsp; Proof-of-Individuality Human Airdrop</div>
  </section>

  <footer class="site-footer">
    <div class="copyright">© 2017 - www.companyname.com</div>
    <div class="page-code">M1</div>
  </footer>
</main>
</body>
</html>
```